App-Design für Vergleichsportal für Reparaturen
Zielgruppe
Flickwerkstolz ist das Vergleichsportal für Reparaturen in deiner Nähe. Egal ob du eine Werkstatt für dein Smartphone, Tablet, Laptop, Computer, Smartwatch oder Spielkonsole suchst. Mit uns findest du deine passende Reparaturwerkstat in deiner Nähe mit dem besten Preis für dich. Du kannst dich direkt über unser Portal deinen Reparaturauftrag erhalten und wirst durch unser Lumen Kaufhut Käuferschutz und unser VORIBA Treuhandschutz abgesichert.
Aufgabenstellung
Unter Flickwerkstolz.de kann das aktuelle Design angeschaut werden. Die Farbe sollten übernommen werden.
Über die Startseite kann der Kunde sein Gerät, Service sowie seine Adresse eingeben. Auf der Vergleichsseite bekommt der Kunde die Übersicht welche Reparaturwerkstätten es gibt, zu welche Preisen die ausgewählte Dienstleistung angeboten wird. Wenn der Kunde auf den Button 'Jetzt Online Bestpreis buchen' drückt, dann kommt der Kunde in den Warenkorb. Im Warenkorb können noch weitere Dienstleistungen und Produkte dazugebucht werden. Und anschließend kommt der Kunde in die Kasse und kann der Bestellvorgang beenden. Die Benutzerführung sollte einfach sein. Im Fokus steht die Vergleichsseite. Dort sollte der Kunde ca. 4 Werkstätten auf einen Blick sehen können. Könnte ausschauen wie bei Preisluke7 in der Kategorie Mobilfunk.
Die Vergleichseite sollte auf jeden Fall folgende Elemente enthalten:
- Entfernung zur Werkstatt in Meter bzw. Kilometer
- Logo der Werkstatt
- Name der Werkstatt
- Bewertungssterne der Werkstatt
- Reparaturzeit und Ersatzeilverfügbarkeit
- Reparaturpreis (Platz sollte auch bei Auswahl von 2 Dienstleistungen vorhanden sein)
- Rabattanzeige
- Qualitätssiegel (noch nicht vorhanden)
- Anzeige von Verknappung (z. B. noch 3 Termin frei)
- Qualitätsmerkmale (z. B. 12 Monate Garantie)
Die Merkmale Öffnungszeiten, Adresse, Kostenpflichtige Zusatzleistungen können aus Platzgründen in den Warenkorbseite wandern außer es gibt eine schöne und einfache Lösung.
In der Warenkorbseite kann dazu auch die Preisluke7 Seite dienen.
Bei allen sollte auf die Benutzerfreundlichkeit geachtet werden.
Bei offenen Frage stehe ich zur Verfügung und freue mich auf viele Designs.
Vielen DANK im Voraus!

```html
<!DOCTYPE html>
<html lang="de">
<head>
<meta charset="utf-8">
<title>Flickwerkstolz – Startseite mobil</title>
<link href="https://fonts.googleapis.com/css2?family=Source+Sans+3:wght@300;400;600;700&display=swap" rel="stylesheet">
<style>
  :root {
    --stage: #262626;
    --petrol: #1f4a5c;
    --green: #8ab839;
    --green-dark: #6f9a22;
    --surface: #eef0f2;
    --white: #ffffff;
    --ink: #2f4a57;
    --muted: #a4adb3;
    --red: #d0242f;
  }
  * { box-sizing: border-box; margin: 0; padding: 0; }
  html, body { width: 1200px; height: 728px; overflow: hidden; background: var(--stage); }
  body { font-family: "Source Sans 3", sans-serif; position: relative; }

  .screen-frame { position: absolute; left: 439px; top: 16px; width: 322px; height: 696px; overflow: hidden; }
  .screen { width: 402px; height: 870px; transform: scale(0.8); transform-origin: 0 0; background: var(--surface); position: relative; overflow: hidden; }

  .status-bar { position: absolute; top: 0; left: 0; right: 0; height: 34px; background: var(--white); display: flex; justify-content: space-between; align-items: center; padding: 0 14px 0 19px; }
  .status-time { font-weight: 600; font-size: 15px; color: #111; }
  .status-icons { display: flex; gap: 5px; align-items: center; }

  .app-header { position: absolute; top: 34px; left: 0; right: 0; height: 53px; background: var(--white); display: flex; align-items: center; justify-content: space-between; padding: 0 16px 0 16px; }
  .brand { display: flex; align-items: center; gap: 6px; font-size: 19px; font-weight: 400; color: var(--green); }
  .brand-dot { width: 12px; height: 12px; border-radius: 50%; background: var(--green); }
  .menu-toggle { width: 24px; display: flex; flex-direction: column; gap: 6px; }
  .menu-toggle span { height: 2px; background: var(--petrol); }

  .hero-band { position: absolute; top: 87px; left: 0; right: 0; height: 88px; background: var(--petrol); text-align: center; padding-top: 26px; color: var(--green); }
  .hero-title { font-size: 13px; font-weight: 700; }
  .hero-sub { font-size: 11px; font-weight: 400; margin-top: 4px; }

  .field { position: absolute; left: 31px; width: 339px; height: 49px; background: var(--white); display: flex; align-items: center; justify-content: space-between; padding: 0 12px; font-size: 15px; font-weight: 300; color: var(--ink); }
  .field.placeholder { color: var(--muted); }
  .field-plus { color: var(--green); font-size: 18px; font-weight: 300; }

  .service-chip { position: absolute; left: 39px; width: 323px; height: 30px; background: var(--green); display: flex; align-items: center; padding: 0 8px 0 9px; font-size: 12px; font-weight: 300; color: var(--white); gap: 8px; }
  .chip-label { flex: 1; }
  .chip-actions { display: flex; gap: 8px; }

  .cta { position: absolute; left: 31px; top: 738px; width: 339px; height: 49px; background: var(--petrol); color: var(--white); font-size: 13px; font-weight: 400; display: flex; align-items: center; justify-content: center; letter-spacing: 0.1px; }

  .trust-badge { position: absolute; top: 828px; width: 58px; height: 64px; }
</style>
</head>
<body>
<div class="screen-frame">
  <main class="screen">
    <div class="status-bar">
      <span class="status-time">9:41</span>
      <span class="status-icons">
        <svg width="17" height="11" viewBox="0 0 17 11"><rect x="0" y="7" width="3" height="4" fill="#111"/><rect x="4.5" y="5" width="3" height="6" fill="#111"/><rect x="9" y="2.5" width="3" height="8.5" fill="#111"/><rect x="13.5" y="0" width="3" height="11" fill="#111"/></svg>
        <svg width="15" height="11" viewBox="0 0 15 11"><path d="M7.5 10.5 L5 7.6 a3.6 3.6 0 0 1 5 0 Z" fill="#111"/><path d="M2.7 5.2 a6.7 6.7 0 0 1 9.6 0" stroke="#111" stroke-width="1.8" fill="none"/><path d="M0.6 3 a9.8 9.8 0 0 1 13.8 0" stroke="#111" stroke-width="1.8" fill="none"/></svg>
        <svg width="25" height="12" viewBox="0 0 25 12"><rect x="0.5" y="0.5" width="21" height="11" rx="3" stroke="#111" fill="none"/><rect x="2.5" y="2.5" width="17" height="7" rx="1.5" fill="#111"/><rect x="22.5" y="4" width="2" height="4" rx="1" fill="#111"/></svg>
      </span>
    </div>

    <header class="app-header">
      <div class="brand"><span class="brand-dot"></span>Flickwerkstolz</div>
      <div class="menu-toggle" aria-label="Menü"><span></span><span></span><span></span></div>
    </header>

    <section class="hero-band">
      <p class="hero-title">Reparaturen Im Vergleich, in deiner Nähe!</p>
      <p class="hero-sub">Garantiert die besten Tarife</p>
    </section>

    <div class="field" style="top:215px">Reparaturkategorie wählen<svg width="10" height="6" viewBox="0 0 10 6"><path d="M1 1l4 4 4-4" stroke="var(--green)" fill="none"/></svg></div>
    <div class="field" style="top:294px">Hersteller wählen<svg width="10" height="6" viewBox="0 0 10 6"><path d="M1 1l4 4 4-4" stroke="var(--green)" fill="none"/></svg></div>
    <div class="field" style="top:373px">Gerät wählen<svg width="10" height="6" viewBox="0 0 10 6"><path d="M1 1l4 4 4-4" stroke="var(--green)" fill="none"/></svg></div>
    <div class="field" style="top:452px">Dienstleistung wählen<span class="field-plus">+</span></div>

    <div class="service-chip" style="top:514px">
      <svg width="12" height="16" viewBox="0 0 12 16"><rect x="1" y="1" width="10" height="14" rx="1.5" stroke="#fff" stroke-width="1.4" fill="none"/><circle cx="6" cy="12.5" r="0.9" fill="#fff"/></svg>
      <span class="chip-label">Display Original-Qualität</span>
      <span class="chip-actions">
        <svg width="11" height="11" viewBox="0 0 11 11"><circle cx="5.5" cy="5.5" r="5.5" fill="var(--petrol)"/><rect x="4.8" y="4.6" width="1.4" height="4" fill="#fff"/><circle cx="5.5" cy="3" r="0.8" fill="#fff"/></svg>
        <svg width="11" height="11" viewBox="0 0 11 11"><circle cx="5.5" cy="5.5" r="5.5" fill="var(--red)"/><rect x="2.5" y="4.8" width="6" height="1.4" fill="#fff"/></svg>
      </span>
    </div>
    <div class="service-chip" style="top:556px">
      <svg width="16" height="12" viewBox="0 0 15 11"><path d="M7.5 10.5 L5 7.6 a3.6 3.6 0 0 1 5 0 Z" fill="#fff"/><path d="M2.7 5.2 a6.7 6.7 0 0 1 9.6 0" stroke="#fff" stroke-width="1.6" fill="none"/><path d="M0.6 3 a9.8 9.8 0 0 1 13.8 0" stroke="#fff" stroke-width="1.6" fill="none"/></svg>
      <span class="chip-label">W-LAN Antenne</span>
      <span class="chip-actions">
        <svg width="11" height="11" viewBox="0 0 11 11"><circle cx="5.5" cy="5.5" r="5.5" fill="var(--petrol)"/><rect x="4.8" y="4.6" width="1.4" height="4" fill="#fff"/><circle cx="5.5" cy="3" r="0.8" fill="#fff"/></svg>
        <svg width="11" height="11" viewBox="0 0 11 11"><circle cx="5.5" cy="5.5" r="5.5" fill="var(--red)"/><rect x="2.5" y="4.8" width="6" height="1.4" fill="#fff"/></svg>
      </span>
    </div>
    <div class="service-chip" style="top:598px">
      <svg width="16" height="10" viewBox="0 0 16 10"><rect x="0.7" y="1.5" width="13" height="7" rx="1" stroke="#fff" stroke-width="1.4" fill="none"/><rect x="2.5" y="3.3" width="4" height="3.4" fill="#fff"/><rect x="14" y="3.5" width="1.5" height="3" fill="#fff"/></svg>
      <span class="chip-label">Akku</span>
      <span class="chip-actions">
        <svg width="11" height="11" viewBox="0 0 11 11"><circle cx="5.5" cy="5.5" r="5.5" fill="var(--petrol)"/><rect x="4.8" y="4.6" width="1.4" height="4" fill="#fff"/><circle cx="5.5" cy="3" r="0.8" fill="#fff"/></svg>
        <svg width="11" height="11" viewBox="0 0 11 11"><circle cx="5.5" cy="5.5" r="5.5" fill="var(--red)"/><rect x="2.5" y="4.8" width="6" height="1.4" fill="#fff"/></svg>
      </span>
    </div>

    <div class="field placeholder" style="top:659px; width:217px">Strasse eingeben</div>
    <div class="field placeholder" style="top:659px; left:265px; width:105px">Hausnr.</div>

    <div class="cta">AUF ZUM REPARATURWERKSTATTVERGLEICH ›</div>

    <svg class="trust-badge" style="left:54px" viewBox="0 0 58 64" aria-label="Bestpreis">
      <path d="M29 2 L55 12 V32 C55 48 43 58 29 62 C15 58 3 48 3 32 V12 Z" fill="none" stroke="var(--green)" stroke-width="4"/>
      <text x="27" y="47" text-anchor="middle" font-family="Source Sans 3, sans-serif" font-size="26" fill="var(--petrol)">€</text>
    </svg>
    <svg class="trust-badge" style="left:171px" viewBox="0 0 58 64" aria-label="Geprüfte Werkstätten">
      <path d="M29 2 L55 12 V32 C55 48 43 58 29 62 C15 58 3 48 3 32 V12 Z" fill="none" stroke="var(--green)" stroke-width="4"/>
      <path d="M17 36 l8 8 l16 -17" fill="none" stroke="var(--petrol)" stroke-width="3"/>
    </svg>
    <svg class="trust-badge" style="left:289px" viewBox="0 0 58 64" aria-label="Sichere Zahlung">
      <path d="M29 2 L55 12 V32 C55 48 43 58 29 62 C15 58 3 48 3 32 V12 Z" fill="none" stroke="var(--green)" stroke-width="4"/>
      <path d="M22 34 v-5 a7 7 0 0 1 14 0 v5" fill="none" stroke="var(--petrol)" stroke-width="2.5"/>
      <rect x="19" y="34" width="20" height="15" rx="2" fill="none" stroke="var(--petrol)" stroke-width="2.5"/>
    </svg>
  </main>
</div>
</body>
</html>
```